Home inspection business! professional look attracting customers just by looks. Read must haves

its a new business I started on my own for home inspections I would like something very professional to give to real estate agents and clients, its going to have my license number on it my business phone number my name my website as well etc on the back side it will be servicing areas and also what kind of services I offer I also have a business card from someone else the way I would like mine to be. I will attach my logo

Industry/Entity Type

Home Inspection

Contact Information for Business Card

listed in nice to haves

Requirements
Must have
• phone number - 718 352 9047
• website- crestwoodlatch.example
• license number #2749035186
• my name Gavin teraskovic
• picture of my logo and me on the front
• on the back of the card. stating I am servicing All of New York and Long Island
• also services I will offer will be home inspection -mold inspection -lead inspection -radon inspection -Termite Inspection -Infared Scan.
• and also we provide inspections for single family homes condos co-ops town-homes
• and commercial property
Nice to have
• same colors as the logos and also if you recommend fonts to look like the logo not sure up to you

```html
<!DOCTYPE html>
<html lang="en">
<head>
<meta charset="utf-8">
<title>Crestwood Latch Home Inspectors – Business Card</title>
<link rel="stylesheet" href="https://fonts.googleapis.com/css2?family=Oswald:wght@500&family=Work+Sans:wght@400;600&display=swap">
<style>
  :root {
    --backdrop: #d3d3ce;
    --paper: #f2f2f2;
    --ink-dark: #252525;
    --accent: #4a9ad8;
    --text-grey: #8a8a8a;
    --text-light: #ffffff;
  }
  * { margin: 0; padding: 0; box-sizing: border-box; }
  html, body {
    width: 1200px; height: 1059px; overflow: hidden;
    background: var(--backdrop);
    font-family: "Work Sans", sans-serif;
  }
  .sheet { position: relative; width: 1200px; height: 1059px; }
  .card {
    position: absolute; width: 540px; height: 309px;
    overflow: hidden;
    box-shadow: 0 10px 24px rgba(0,0,0,0.12);
  }

  /* Front face */
  .card--front { left: 40px; top: 375px; background: var(--paper); }
  .identity {
    position: absolute; left: 16px; top: 118px; width: 254px;
    text-align: right; white-space: nowrap;
  }
  .identity__name {
    font-family: "Oswald", sans-serif; font-weight: 500;
    font-size: 28px; letter-spacing: 0.5px; line-height: 1;
    color: var(--accent); text-transform: uppercase;
  }
  .identity__role { font-size: 13px; color: var(--text-grey); margin-top: 4px; }
  .divider {
    position: absolute; left: 284px; top: 112px;
    width: 1.5px; height: 62px; background: var(--accent);
  }
  .contacts {
    position: absolute; left: 298px; top: 110px; width: 226px;
    list-style: none; font-size: 12px; color: var(--text-grey);
    white-space: nowrap;
  }
  .contacts li { display: flex; align-items: center; gap: 6px; line-height: 22px; }
  .contacts svg { width: 10px; height: 10px; flex: none; }
  .license {
    position: absolute; right: 34px; bottom: 30px;
    font-size: 13px; color: var(--text-grey); letter-spacing: 0.5px;
  }

  /* Back face */
  .card--back {
    left: 620px; top: 375px;
    background: var(--ink-dark); color: var(--text-light);
    text-align: center;
  }
  .brand {
    position: absolute; left: 0; right: 0; top: 50px;
    display: flex; justify-content: center; align-items: center; gap: 10px;
    font-weight: 600; font-size: 18px; letter-spacing: 1.5px;
    text-transform: uppercase; color: var(--text-light); white-space: nowrap;
  }
  .brand__dot { width: 12px; height: 12px; border-radius: 50%; background: var(--text-light); }
  .services {
    position: absolute; left: 24px; right: 24px; top: 118px;
    font-size: 13.5px; line-height: 1.32; letter-spacing: 0.3px;
  }
  .services p + p { margin-top: 10px; }
</style>
</head>
<body>
<main class="sheet">

  <section class="card card--front" aria-label="Card front">
    <div class="identity">
      <h1 class="identity__name">Gavin Teraskovic</h1>
      <p class="identity__role">Director</p>
    </div>
    <span class="divider"></span>
    <ul class="contacts">
      <li>
        <svg viewBox="0 0 12 12" aria-hidden="true"><path d="M3 1 L5 3.5 L4 5 Q5 7 7 8 L8.5 7 L11 9 L9.5 11 Q4 10.5 1 3 Z" fill="#4a9ad8"/></svg>
        718 352 9047
      </li>
      <li>
        <svg viewBox="0 0 12 12" aria-hidden="true"><rect x="1" y="2.5" width="10" height="7" fill="none" stroke="#4a9ad8" stroke-width="1.2"/><path d="M1 2.5 L6 6.5 L11 2.5" fill="none" stroke="#4a9ad8" stroke-width="1.2"/></svg>
        info@crestwoodlatch.example
      </li>
      <li>
        <svg viewBox="0 0 12 12" aria-hidden="true"><circle cx="6" cy="6" r="5" fill="#4a9ad8"/><path d="M1 6 H11 M6 1 Q3 6 6 11 M6 1 Q9 6 6 11" fill="none" stroke="#f2f2f2" stroke-width="0.8"/></svg>
        www.crestwoodlatch.example
      </li>
    </ul>
    <p class="license">#2749035186</p>
  </section>

  <section class="card card--back" aria-label="Card back">
    <div class="brand">
      <span class="brand__dot"></span>
      <span>Crestwood Latch Home Inspectors</span>
    </div>
    <div class="services">
      <p>stating I am servicing All of New York and Long Island<br>
      also services I will offer will be home inspection<br>
      mold inspection -lead inspection -radon inspection<br>
      Termite Inspection -Infared Scan.</p>
      <p>and also we provide inspections for single family<br>
      homes condos co-ops town-homes and commercial property</p>
    </div>
  </section>

</main>
</body>
</html>
```